simple attractive bottled purified natural water label

Looking for a logo design, for a bottled water house brand.The Name of the water is "Orvi-K" Natural Purified water I have attached 2 images, In the Tamsol Image, I Like the top Left water design, the bold Red Name really stands out.I like the placement of the Font with the Natural Purified water,On the 2nd image Russian one, I again like the red bold, the bird flying out is interesting, not sure if a concept could rather use a seabird / gul or a albatros type, with the same effectThe blue colours in bother these designs are great.Many tahnks

Target Market(s)

Young crowd

Font styles to use
Sans Serif

Colors
0455a3
3276b5
ffffff
33a6d7
85cae6
85acd3
0692cd
ec1f27

Requirements
Must have
• some red in the label to make it pop.
• simple design
Nice to have
• the idea of a Gull ( Bird ) flying out to signify free pure natural.

```html
<!DOCTYPE html>
<html lang="en">
<head>
<meta charset="utf-8">
<title>Orvi-K Natural Purified Water – Label</title>
<link rel="stylesheet" href="https://fonts.googleapis.com/css2?family=Montserrat:wght@700;800&display=swap">
<style>
  :root {
    --deep-blue: #0455a3;
    --mid-blue: #3276b5;
    --sky-blue: #33a6d7;
    --pale-blue: #85cae6;
    --soft-blue: #85acd3;
    --bright-blue: #0692cd;
    --cyan-band: #22b6ea;
    --brand-red: #ec1f27;
    --white: #ffffff;
    --stage: #eef1f4;
  }
  * { margin: 0; padding: 0; box-sizing: border-box; }
  html, body {
    width: 1200px;
    height: 900px;
    overflow: hidden;
    background: var(--stage);
  }
  .label {
    position: absolute;
    left: 133px;
    top: 0;
    width: 934px;
    height: 900px;
    overflow: hidden;
    background: var(--white);
  }
  .drop-pattern {
    position: absolute;
    left: 0;
    width: 100%;
  }
  .drop-pattern--top {
    top: 0;
    height: 322px;
    background: linear-gradient(90deg, var(--mid-blue), var(--sky-blue) 25%, var(--pale-blue) 50%, var(--bright-blue) 75%, var(--mid-blue));
    opacity: 0.85;
  }
  .drop-pattern--bottom {
    top: 800px;
    height: 100px;
    background: linear-gradient(90deg, var(--sky-blue), var(--bright-blue) 30%, var(--pale-blue) 60%, var(--mid-blue));
    opacity: 0.85;
  }
  .cyan-band {
    position: absolute;
    left: 0;
    width: 100%;
    background: var(--cyan-band);
  }
  .cyan-band--top { top: 322px; height: 61px; }
  .cyan-band--bottom { top: 749px; height: 51px; background: linear-gradient(180deg, var(--cyan-band), #5fb7e4); }
  .name-panel {
    position: absolute;
    left: 0;
    top: 383px;
    width: 100%;
    height: 366px;
    background: linear-gradient(180deg, var(--white) 5%, #d3e8f7 50%, #9fcbee 100%);
  }
  .brand-name {
    position: absolute;
    left: 98px;
    top: 78px;
    font-family: "Montserrat", sans-serif;
    font-weight: 800;
    font-size: 178px;
    line-height: 1;
    letter-spacing: -4px;
    color: var(--brand-red);
  }
  .tagline {
    position: absolute;
    left: 102px;
    top: 300px;
    font-family: "Montserrat", sans-serif;
    font-weight: 800;
    font-size: 29px;
    letter-spacing: 2.5px;
    color: var(--mid-blue);
  }
</style>
</head>
<body>
  <main class="label">
    <div class="drop-pattern drop-pattern--top" role="img" aria-label="Decorative pattern of rows of two-tone blue water drops"></div>
    <div class="cyan-band cyan-band--top"></div>
    <section class="name-panel">
      <h1 class="brand-name">Orvi-K</h1>
      <p class="tagline">NATURAL PURIFIED WATER</p>
    </section>
    <div class="cyan-band cyan-band--bottom"></div>
    <div class="drop-pattern drop-pattern--bottom" role="img" aria-label="Decorative pattern of rows of two-tone blue water drops"></div>
  </main>
</body>
</html>
```